Custom workshop/manufacture for custom furniture, architectural millwork and kitchen cabinetry

simple and clean. I like this website:
http://www.pebblelarchworks.com

Attached are random ideas

Target Market(s)

residential, commercial, hospitality, interior designers, architects, contractors

Coding

Coded - Design and coding required

Number of Pages Required

5+ page

Font styles to use
Other font styles liked:
• Avenir next

Requirements
Must have
• drop down menu for work - residential - commercial

```html
<!DOCTYPE html>
<html lang="en">
<head>
<meta charset="utf-8">
<title>Harlan Oak Furniture</title>
<link href="https://fonts.googleapis.com/css2?family=Oswald:wght@300;400;500&family=Lato:wght@400;700&family=Open+Sans:ital,wght@0,400;0,600;1,400&display=swap" rel="stylesheet">
<style>
:root{
  --yellow:#f7ee00;
  --ink:#1b1b1b;
  --text:#3a3a3a;
  --grey-bg:#efefef;
  --white:#ffffff;
  --dark:#101010;
  --brown:#3b2a1e;
  --muted:#9a9a9a;
}
*{margin:0;padding:0;box-sizing:border-box}
html,body{width:1200px;height:4348px;overflow:hidden}
body{background:var(--white);font-family:"Lato",sans-serif;color:var(--text);position:relative}
section,header,footer{position:absolute;left:0;width:1200px}
.abs{position:absolute}
.heading{font-family:"Oswald",sans-serif;font-weight:400;text-transform:uppercase;color:var(--ink);text-align:center;width:1200px;left:0;font-size:40px;line-height:1}
.heading-light{font-weight:300;font-size:50px}
.btn{position:absolute;background:var(--yellow);color:var(--ink);font-family:"Oswald",sans-serif;font-size:18px;display:flex;align-items:center;justify-content:center;text-decoration:none}
.photo{position:absolute}

/* header */
.site-header{top:0;height:96px;background:var(--white)}
.brand{left:80px;top:20px;display:flex;align-items:center;gap:14px}
.brand-mark{width:52px;height:52px;background:var(--ink)}
.brand-name{font-family:"Oswald",sans-serif;font-weight:500;font-size:26px;line-height:1.05;color:var(--ink)}
.main-nav{right:75px;top:32px;display:flex;gap:0}
.main-nav a{font-family:"Lato",sans-serif;font-size:14px;font-weight:700;color:var(--ink);text-decoration:none;padding:10px 19px;text-transform:uppercase}
.main-nav a.active{background:var(--yellow)}

/* hero */
.hero{top:96px;height:568px;background:linear-gradient(180deg,#8a8a88 0%,#5b5a57 45%,#2e2c2a 100%)}
.hero-title{top:237px;width:1200px;text-align:center;font-family:"Oswald",sans-serif;font-weight:500;font-size:46px;color:var(--yellow);text-transform:uppercase}
.hero-sub{top:290px;width:1200px;text-align:center;font-family:"Open Sans",sans-serif;font-size:30px;color:var(--white)}
.dots{top:518px;left:560px;display:flex;gap:10px}
.dots span{width:11px;height:11px;border-radius:50%;background:var(--white)}
.dots span.on{background:var(--yellow)}

/* welcome */
.welcome{top:664px;height:339px}
.welcome .heading{top:62px}
.body-copy{font-size:16px;line-height:1.75;color:var(--text)}
.welcome-copy{left:87px;top:124px;width:1026px;text-align:center}

/* what we do */
.services{top:1003px;height:1091px;background:var(--grey-bg)}
.services .section-title{top:60px}
.services .materials-title{top:612px}
.service-photo{left:165px;top:148px;width:334px;height:354px;background:linear-gradient(135deg,#6a4b35,#c9a27a 60%,#8d6a4c)}
.service-title{left:528px;top:180px;font-family:"Oswald",sans-serif;font-weight:300;font-size:52px;color:var(--ink);text-transform:uppercase}
.service-copy{left:528px;top:252px;width:470px;font-size:14px;line-height:1.75}
.service-copy p+p{margin-top:10px}
.material{position:absolute;top:696px;width:331px;height:232px;display:flex;align-items:center;justify-content:center;font-family:"Oswald",sans-serif;font-size:30px;color:var(--white);text-transform:uppercase}
.mat-wood{left:75px;background:linear-gradient(180deg,#8d8d8d,#5a4034 60%,#8d8d8d)}
.mat-metal{left:435px;background:linear-gradient(180deg,#8d8d8d,#4a4440 55%,#a4a4a4)}
.mat-brass{left:797px;background:linear-gradient(180deg,#8d8d8d,#5c463a 55%,#8d8d8d)}
.arrow{position:absolute;top:795px}
.materials-copy{left:75px;top:969px;width:1053px;text-align:center;font-size:14px;line-height:1.75}

/* upholstery */
.upholstery{top:2094px;height:620px}
.upholstery .heading{top:50px}
.uph-photo-1{left:165px;top:124px;width:421px;height:209px;background:linear-gradient(135deg,#a8865e,#6c5540 50%,#c4a27a)}
.uph-photo-2{left:615px;top:124px;width:420px;height:209px;background:linear-gradient(135deg,#7a5a40,#c9a98a 50%,#5a3f2c)}
.uph-title{font-family:"Oswald",sans-serif;font-weight:300;font-size:34px;color:var(--ink);text-transform:uppercase;top:356px}
.uph-copy{top:410px;width:420px;font-size:14px;line-height:1.75}

/* quote */
.quote-band{top:2714px;height:232px;background:linear-gradient(90deg,#2a1d14,#5a4331 50%,#2a1d14)}
.quote{top:68px;left:250px;width:700px;text-align:center;font-family:"Open Sans",sans-serif;font-weight:600;font-size:30px;line-height:1.35;color:var(--white);text-transform:uppercase}
.quote-author{top:162px;width:1200px;text-align:center;font-family:"Open Sans",sans-serif;font-weight:600;font-size:17px;color:var(--yellow);text-transform:uppercase}

/* gallery */
.gallery{top:2946px;height:612px}
.gallery .heading{top:52px}
.tile{position:absolute;border:2px solid #d8d8d8;background:var(--white);display:flex;align-items:center;justify-content:center}
.tile span{display:block;width:74%;height:52%}
.t1{left:75px;top:119px;width:331px;height:227px}.t1 span{background:linear-gradient(180deg,#5a3b26,#2a1a10)}
.t2{left:75px;top:363px;width:331px;height:211px}.t2 span{background:linear-gradient(180deg,#f2f2f2,#1c1c1c)}
.t3{left:420px;top:119px;width:270px;height:455px}.t3 span{width:54%;height:60%;background:linear-gradient(180deg,#9a8b76,#2a1a12)}
.t4{left:705px;top:119px;width:206px;height:192px}.t4 span{width:70%;height:62%;background:linear-gradient(180deg,#a77c52,#6b4a2c)}
.t5{left:922px;top:119px;width:206px;height:192px}.t5 span{width:72%;height:56%;background:linear-gradient(180deg,#d9262b,#9a1418)}
.t6{left:705px;top:331px;width:423px;height:243px}.t6 span{width:64%;height:72%;background:linear-gradient(180deg,#4a6fa6,#e8e1cf 60%,#4a6fa6)}

/* clients */
.clients{top:3558px;height:403px;background:linear-gradient(90deg,#1e1a17,#3a342d 50%,#1e1a17)}
.clients .heading{top:66px;color:var(--white)}
.testimonial{position:absolute;top:186px;width:330px;text-align:center;font-family:"Open Sans",sans-serif;font-style:italic;font-size:14px;line-height:1.6;color:var(--white)}
.testimonial .name{display:block;margin-top:18px;font-style:normal;font-weight:600;font-size:13px;color:var(--yellow);text-transform:uppercase}
.testimonial .loc{display:block;font-style:normal;font-size:11px;color:#bbbbbb}

/* footer */
.site-footer{top:3961px;height:387px;background:var(--dark);color:var(--white)}
.foot-title{font-family:"Oswald",sans-serif;font-weight:300;font-size:28px;text-transform:uppercase;top:44px}
.foot-text{font-size:14px;line-height:1.75;color:#cfcfcf}
.info-line{display:flex;align-items:center;gap:14px;font-size:14px;color:#cfcfcf}
.field{position:absolute;border:1px solid #8a8a8a;background:transparent;color:#cfcfcf;font-size:12px;padding:8px 12px}
.send{background:var(--yellow);color:var(--ink);font-family:"Oswald",sans-serif;font-size:16px}
.social{left:75px;top:262px;display:flex;gap:18px}
.social span{width:18px;height:18px;border-radius:50%;background:#cfcfcf}
.rule{left:75px;top:308px;width:1053px;height:1px;background:#2b2b2b}
.copyright{top:342px;width:1200px;text-align:center;font-size:11px;color:#7a7a7a}
</style>
</head>
<body>

<header class="site-header">
  <div class="abs brand">
    <div class="brand-mark"></div>
    <div class="brand-name">Harlan Oak<br>Furniture</div>
  </div>
  <nav class="abs main-nav">
    <a class="active" href="#">Home</a>
    <a href="#">Who We Are</a>
    <a href="#">What We Do</a>
    <a href="#">How We Work</a>
    <a href="#">Gallery</a>
    <a href="#">Blog</a>
    <a href="#">Contact</a>
  </nav>
</header>

<section class="hero" role="img" aria-label="Modern kitchen interior with dark wood cabinetry and a stone island">
  <h1 class="abs hero-title">Harlan Oak Furniture</h1>
  <p class="abs hero-sub">Etiam elementum est id sapien tincidunt.</p>
  <div class="abs dots"><span class="on"></span><span></span><span></span><span></span></div>
</section>

<section class="welcome">
  <h2 class="abs heading">Welcome to our website</h2>
  <p class="abs body-copy welcome-copy">We specialize in translating designers' concepts into beautiful furniture. It is our mission to provide you with top quality materials and products. Partnerships with Los Angeles' most exceptional craftsmen has brought this aim to life. The results can be found in the world's most renowned locations.</p>
  <a class="btn" href="#" style="left:528px;top:241px;width:142px;height:40px">Read More</a>
</section>

<section class="services">
  <h2 class="abs heading section-title">What we do</h2>
  <div class="photo service-photo" role="img" aria-label="Craftsman assembling a wooden cabinet in the workshop"></div>
  <h3 class="abs service-title">Manufacturing</h3>
  <div class="abs service-copy">
    <p>HARLANOF specializes in design-driven custom manufacturing for a variety of markets including, but not limited to, retail, commercial, architectural, hospitality, and high-end residential.</p>
    <p>HARLAN uses the highest quality materials in all of its products, and finishes each item by hand.</p>
  </div>
  <a class="btn" href="#" style="left:528px;top:421px;width:142px;height:41px">Read More</a>

  <h2 class="abs heading heading-light materials-title">Materials</h2>
  <svg class="arrow" style="left:46px" width="14" height="26" viewBox="0 0 14 26"><path d="M12 2 2 13l10 11" fill="none" stroke="#555" stroke-width="2"/></svg>
  <div class="material mat-wood" role="img" aria-label="Dark wood console table">Wood</div>
  <div class="material mat-metal" role="img" aria-label="Round table with metal base">Metal</div>
  <div class="material mat-brass" role="img" aria-label="Upholstered bench with carved legs">Brass</div>
  <svg class="arrow" style="left:1140px" width="14" height="26" viewBox="0 0 14 26"><path d="M2 2l10 11L2 24" fill="none" stroke="#555" stroke-width="2"/></svg>
  <p class="abs materials-copy">Our capabilities with regard to complex areas of Furniture making are limitless. Frequently, our clients Will call us because they are looking for a technique or Material that cannot be found anywhere else. Essentially, we do everything the old fashioned way, by hand. We pride ourselves on bringing the highest Standards of craftsmanship to every material that is Suitable for use in our field.</p>
</section>

<section class="upholstery">
  <h2 class="abs heading">Upholstery &amp; Reupholster</h2>
  <div class="photo uph-photo-1" role="img" aria-label="Hands working on chair springs"></div>
  <div class="photo uph-photo-2" role="img" aria-label="Wooden chair leg being finished on a lathe"></div>
  <h3 class="abs uph-title" style="left:165px">Handmade in Los Angeles</h3>
  <p class="abs body-copy uph-copy" style="left:165px">Unique, sculptural, timeless, from initial consultations and design to production and finishing, we embrace a hands-on approach that takes every detail into account. Shape, comfort, purpose and lifestyle..</p>
  <a class="btn" href="#" style="left:165px;top:533px;width:142px;height:40px">Read More</a>
  <h3 class="abs uph-title" style="left:615px">Finishing</h3>
  <p class="abs body-copy uph-copy" style="left:615px">All finishes can be produced with water based materials containing little or no VOC emissions, are bio-degradable, and have exceptional durability.</p>
  <a class="btn" href="#" style="left:615px;top:533px;width:142px;height:40px">Read More</a>
</section>

<section class="quote-band" role="img" aria-label="Close-up of a woodworker's hands sanding a board">
  <p class="abs quote">"Quality means doing it right when no one is looking"</p>
  <p class="abs quote-author">-Marcus Whitfield</p>
</section>

<section class="gallery">
  <h2 class="abs heading">Gallery</h2>
  <div class="tile t1"><span role="img" aria-label="Dark wood dining table"></span></div>
  <div class="tile t2"><span role="img" aria-label="Striped upholstered daybed"></span></div>
  <div class="tile t3"><span role="img" aria-label="Upholstered dining chair"></span></div>
  <div class="tile t4"><span role="img" aria-label="Wooden sideboard with wine rack"></span></div>
  <div class="tile t5"><span role="img" aria-label="Red lacquered dresser"></span></div>
  <div class="tile t6"><span role="img" aria-label="Blue tufted upholstered bed"></span></div>
</section>

<section class="clients" role="img" aria-label="Workshop interior with craftsmen at work">
  <h2 class="abs heading">What our clients says</h2>
  <p class="testimonial" style="left:75px">" Vestibulum ante ipsum primis in faucibus orci luctus et ultrices posuere cubilia aliquam nibh a dui iaculis viverra id a velit. "<span class="name">Name Heading</span><span class="loc">Location</span></p>
  <p class="testimonial" style="left:435px">" Vestibulum ante ipsum primis in faucibus orci luctus et ultrices posuere cubilia aliquam nibh a dui iaculis viverra id a velit. "<span class="name">Name Heading</span><span class="loc">Location</span></p>
  <p class="testimonial" style="left:797px">" Vestibulum ante ipsum primis in faucibus orci luctus et ultrices posuere cubilia aliquam nibh a dui iaculis viverra id a velit. "<span class="name">Name Heading</span><span class="loc">Location</span></p>
</section>

<footer class="site-footer">
  <h3 class="abs foot-title" style="left:75px">Contact Information</h3>
  <p class="abs foot-text" style="left:75px;top:104px">218 Cedar Mill Road<br>Fairbrook,<br>CA 90412</p>
  <div class="abs" style="left:300px;top:104px">
    <div class="info-line"><svg width="14" height="14" viewBox="0 0 24 24"><path d="M6.6 10.8a15 15 0 0 0 6.6 6.6l2.2-2.2c.3-.3.7-.4 1-.2 1.1.4 2.3.6 3.6.6.6 0 1 .4 1 1V20c0 .6-.4 1-1 1A17 17 0 0 1 3 4c0-.6.4-1 1-1h3.5c.6 0 1 .4 1 1 0 1.3.2 2.5.6 3.6.1.3 0 .7-.2 1z" fill="#cfcfcf"/></svg>1-800-555-0148</div>
    <div class="info-line" style="margin-top:8px"><svg width="14" height="12" viewBox="0 0 24 18"><path d="M0 0h24v18H0z" fill="#cfcfcf"/><path d="M0 0l12 9 12-9" fill="none" stroke="#101010" stroke-width="2"/></svg>hello@harlanoak.com</div>
  </div>
  <div class="abs info-line" style="left:75px;top:190px"><svg width="12" height="16" viewBox="0 0 12 16"><path d="M6 0a6 6 0 0 0-6 6c0 4.5 6 10 6 10s6-5.5 6-10a6 6 0 0 0-6-6zm0 8.5A2.5 2.5 0 1 1 6 3.5a2.5 2.5 0 0 1 0 5z" fill="var(--yellow)"/></svg><span style="margin-left:18px">Map Direction</span></div>
  <div class="abs social"><span></span><span></span><span></span><span></span><span></span></div>

  <h3 class="abs foot-title" style="left:612px">Contact Form</h3>
  <div class="field" style="left:612px;top:105px;width:246px;height:32px">Enter Name</div>
  <div class="field" style="left:612px;top:148px;width:246px;height:32px">Email Address</div>
  <div class="field" style="left:612px;top:192px;width:246px;height:32px">Phone No.</div>
  <div class="field" style="left:885px;top:105px;width:243px;height:119px">Message</div>
  <div class="btn send" style="left:1050px;top:238px;width:78px;height:38px">SEND</div>

  <div class="abs rule"></div>
  <p class="abs copyright">Copyright © 2016. Harlan Oak Furniture. All Rights Reserved</p>
</footer>

</body>
</html>
```